brightwave pools cards

i need to create a design to use on my business cards,brochures and as a letterhead. i am a new swimming pool renovation business named BRIGHTWAVE POOLS. I require a smart professional deign to reflect that my business is the best in the industry.
should include something like.... Brightwave Pools ABN - 57184620931
residential pool renovation specialists
specialising in the art of - fully tiled pools
- waterline tiles
- natural stone pool copings
and outdoor areas - concrete slabs - detailed mosaic work - pool lighting and water features - pool painting

trent - 0461829304 gordon -0438152967 brightwavepoolsnorth@mailbox-example.com

the design could feature - water, natural stone (travertine, sandstone etc), something to personafy the word imagine.
looking foward to seeing some ideas... cheers heaps trent

```html
<!DOCTYPE html>
<html lang="en">
<head>
<meta charset="utf-8">
<title>Brightwave Pools – Business Card</title>
<link rel="stylesheet" href="https://fonts.googleapis.com/css2?family=Jost:wght@400;500&family=PT+Serif:wght@700&family=Arimo:wght@400&family=Didact+Gothic&display=swap">
<style>
  :root {
    --backdrop: #2c2c2e;
    --slate: #435e6e;
    --band-light: #c9e4e4;
    --card-white: #ffffff;
    --card-mint: #c4ecd0;
    --tagline-mint: #a8ddb4;
    --text-light: #ffffff;
    --text-soft: #dfeeee;
  }
  * { box-sizing: border-box; margin: 0; padding: 0; }
  html, body {
    width: 1200px;
    height: 1000px;
    overflow: hidden;
    background: var(--backdrop);
  }
  .stage {
    position: relative;
    width: 1200px;
    height: 1000px;
  }

  .card {
    position: absolute;
    top: 220px;
    width: 510px;
    height: 292px;
    overflow: hidden;
  }

  /* Back of card */
  .card-back {
    left: 60px;
    background: var(--slate);
  }
  .contact-band {
    position: absolute;
    left: 0;
    top: 44px;
    width: 372px;
    height: 132px;
    background: var(--band-light);
    padding: 22px 0 0 26px;
    font-family: "PT Serif", Georgia, serif;
    font-weight: 700;
    color: var(--slate);
    font-size: 15.5px;
    line-height: 21px;
  }
  .contact-band .email { font-size: 13px; margin-top: 14px; }
  .services {
    position: absolute;
    left: 360px;
    top: 186px;
    list-style: none;
    font-family: "Arimo", Arial, sans-serif;
    font-size: 13px;
    line-height: 15.5px;
    color: var(--text-soft);
    white-space: nowrap;
  }

  /* Front of card */
  .card-front {
    left: 630px;
    background: radial-gradient(ellipse 60% 70% at 58% 58%, var(--card-mint) 0%, #e4f7ea 55%, var(--card-white) 100%);
  }
  .front-mark {
    position: absolute;
    left: 96px;
    top: 40px;
    display: flex;
    align-items: center;
    gap: 8px;
    font-family: "Jost", Arial, sans-serif;
    font-size: 15px;
    font-weight: 500;
    color: var(--slate);
  }
  .front-mark .dot {
    width: 18px;
    height: 18px;
    border-radius: 50%;
    background: #4f8c93;
  }
  .name-band {
    position: absolute;
    left: 150px;
    top: 116px;
    right: 0;
    height: 100px;
    background: var(--slate);
    padding: 14px 0 0 22px;
  }
  .name-band .brand {
    font-family: "Jost", Arial, sans-serif;
    font-weight: 400;
    font-size: 39px;
    letter-spacing: 0.5px;
    line-height: 44px;
    color: var(--text-light);
    white-space: nowrap;
  }
  .name-band .tagline {
    font-family: "Arimo", Arial, sans-serif;
    font-size: 16px;
    color: var(--text-soft);
    margin-top: 2px;
    white-space: nowrap;
  }

  /* Brand lockup */
  .lockup {
    position: absolute;
    left: 0;
    right: 0;
    top: 640px;
    display: flex;
    flex-direction: column;
    align-items: center;
  }
  .lockup-name {
    display: flex;
    align-items: center;
    gap: 16px;
    font-family: "Didact Gothic", Arial, sans-serif;
    font-size: 50px;
    color: var(--text-light);
    line-height: 56px;
  }
  .lockup-name .dot {
    width: 34px;
    height: 34px;
    border-radius: 50%;
    background: #6fb9bd;
  }
  .lockup-tagline {
    font-family: "Didact Gothic", Arial, sans-serif;
    font-size: 22px;
    color: var(--tagline-mint);
    margin-top: 6px;
  }
</style>
</head>
<body>
<main class="stage">

  <section class="card card-back" aria-label="Business card back">
    <div class="contact-band">
      <p class="person">TRENT&nbsp; 046-182-9304</p>
      <p class="person">GORDON 043-815-2967</p>
      <p class="email">brightwavepoolsnorth@mailbox-example.com</p>
    </div>
    <ul class="services">
      <li>detailed mosaic works</li>
      <li>fully tiled pads</li>
      <li>waterline files</li>
      <li>outdoor area</li>
      <li>pool lighting</li>
      <li>pool painting</li>
    </ul>
  </section>

  <section class="card card-front" aria-label="Business card front">
    <div class="front-mark"><span class="dot"></span>brightwave pools</div>
    <div class="name-band">
      <p class="brand">brightwave pools</p>
      <p class="tagline">your backyard, reimagined in blue</p>
    </div>
  </section>

  <section class="lockup" aria-label="Brand lockup">
    <div class="lockup-name"><span class="dot"></span>brightwave pools</div>
    <p class="lockup-tagline">your backyard, reimagined in blue</p>
  </section>

</main>
</body>
</html>
```